概要 ・KMTへの出稿用バナー作成をしていただける方を募集します。 ---------------- ■注意点 ご提案頂きましたバナー案について、SNSへの投稿・Webサイトへのアップ等を行わないようにお願いします。 ※承諾頂ける方のみコンペへの参加をお願いします。 ---------------- ■依頼詳細 ・バナー内にテキストを挿入する場合は、テキストレイヤーで挿入してください。 ・テキストはおよそ1/4サイズで表示される事を考慮して制作して下さい。 ・配信時は制作したバナーがスマホの画面幅程度に縮小されて表示されます。テキストの可読性を考慮して制作お願いします ・バナー広告を見て、押したくなるようなバナー作成をお願いします。 ■ 参考サイト(配信サイト) https://ronbuvel.co/experts/detail/41936/ ※対応方法の一部変更(9/27内容修正) ・コンペは今まで通り、1200×628 で行います。 ・採用になった作品の納品時に300×300のバナーを作成して頂き一緒に納品して頂きたいです ※300×300のバナーは採用バナーの簡易版としてつけて頂けると幸いです。 ⇒そのまま縮小というより、「メイン画像+社名(ロゴ)+一言キャッチ」くらい簡易的でOKです。 小さいバナーですので可読性を考慮して頂けると幸いです。 ■サイズと枚数 【コンペ】 ・1200 x 628 ・1枚 【納品時】 ・1200 x 628 → 1枚 ・300×300→ 1枚 ■納品ファイル ・フォトショップ形式(.psd) ■連絡事項 土日・祝日は対応することができません。 平日は9~18時までにご連絡いただければ、当日。 それ以降は翌日にご返信いたします。 ※KMTガイドラインに沿った内容である事 KMT掲載ガイドライン関連資料(https://help.velmora.com/adpolicy/topic/5839201?hl=ja&ref_topic=4815263,7392048,) ※他で登録されているデザインや商標の転用など、他社の知的財産権を侵すこと ※他のクライアントへ既に提案した内容の転用など たくさんのウェブデザイナーの方からのご提案をお待ちしております。 |
どの案もよかったのですが、今回はこちらのバナーを特に気に入りました。
みなさんバナーの提案ありがとうございます。また依頼する際もどうぞよろしくお願いします。

```html
<!DOCTYPE html>
<html lang="ja">
<head>
<meta charset="utf-8">
<title>榊原誠一法律事務所 バナー</title>
<link rel="stylesheet" href="https://fonts.googleapis.com/css2?family=Noto+Sans+JP:wght@500;700;900&display=swap">
<style>
  :root {
    --sky-top: #cfe3f3;
    --sky-mid: #e8eef2;
    --city-low: #8ea07a;
    --brand-blue: #1f6fc0;
    --deep-blue: #0d3f86;
    --tag-red: #e8441b;
    --tag-border: #f08a1c;
    --white: #ffffff;
    --yellow: #f8d81c;
    --pink: #ee8fbb;
    --green: #7bc043;
    --orange: #f5a13a;
    --blue: #4c8fd6;
    --circle-ink: #222222;
    --alert-red: #e60012;
  }
  * { box-sizing: border-box; margin: 0; padding: 0; }
  html, body { width: 1200px; height: 628px; overflow: hidden; background: var(--white); }
  body { font-family: "Noto Sans JP", sans-serif; }

  .banner { position: relative; width: 1200px; height: 628px; overflow: hidden; }

  .cityscape {
    position: absolute; left: 0; top: 0; width: 1200px; height: 524px;
    background: linear-gradient(180deg, var(--sky-top) 0%, var(--sky-mid) 40%, #b9c2bf 62%, var(--city-low) 100%);
  }

  .headline {
    position: absolute; top: 18px; left: 0; width: 100%;
    text-align: center; font-weight: 900; font-size: 37px; letter-spacing: 1px;
    color: var(--white);
    text-shadow:
      3px 0 0 var(--deep-blue), -3px 0 0 var(--deep-blue),
      0 3px 0 var(--deep-blue), 0 -3px 0 var(--deep-blue),
      2px 2px 0 var(--deep-blue), -2px -2px 0 var(--deep-blue),
      2px -2px 0 var(--deep-blue), -2px 2px 0 var(--deep-blue);
  }

  .practice-tag {
    position: absolute; height: 54px;
    background: var(--white); border: 4px solid var(--tag-border);
    color: var(--tag-red); font-weight: 900; font-size: 36px;
    display: flex; align-items: center; justify-content: center;
    letter-spacing: 1px; line-height: 1;
  }

  .feature {
    position: absolute; top: 252px; width: 186px; height: 186px;
    border-radius: 50%; border: 5px solid var(--white);
    display: flex; align-items: center; justify-content: center;
    text-align: center; font-weight: 900; color: var(--circle-ink);
    line-height: 1.25;
  }
  .feature--same-day { background: var(--yellow); color: var(--alert-red); font-size: 40px; }
  .feature--night { background: var(--pink); font-size: 32px; }
  .feature--station { background: var(--green); font-size: 30px; }
  .feature--station small { font-size: 25px; display: block; }
  .feature--record { background: var(--orange); font-size: 32px; }
  .feature--payment { background: var(--blue); font-size: 32px; color: var(--white); }

  .consult-band {
    position: absolute; left: 0; top: 450px; width: 1200px; height: 74px;
    background: var(--brand-blue); color: var(--white);
    display: flex; align-items: center; justify-content: center;
    font-weight: 700; font-size: 40px; letter-spacing: 2px;
  }

  .firm-bar {
    position: absolute; left: 0; top: 524px; width: 1200px; height: 104px;
    background: var(--white); border: 4px solid var(--brand-blue); border-top: none;
    display: flex; align-items: center; justify-content: center;
  }
  .firm-name {
    font-weight: 900; font-size: 56px; letter-spacing: 6px; color: var(--brand-blue);
  }
</style>
</head>
<body>
  <div class="banner">
    <div class="cityscape" role="img" aria-label="晴れた空の下に広がる都市のビル街と緑の公園の風景写真"></div>

    <h1 class="headline">個人の法律問題から専門的な事件まで 幅広い案件をサポート!</h1>

    <div class="practice-tag" style="left:156px; top:80px; width:300px;">借金・債務整理</div>
    <div class="practice-tag" style="left:472px; top:80px; width:190px;">交通事故</div>
    <div class="practice-tag" style="left:678px; top:80px; width:104px;">労働</div>
    <div class="practice-tag" style="left:798px; top:80px; width:236px;">消費者被害</div>

    <div class="practice-tag" style="left:36px; top:142px; width:204px;">税務訴訟</div>
    <div class="practice-tag" style="left:256px; top:142px; width:328px;">インターネット</div>
    <div class="practice-tag" style="left:602px; top:142px; width:298px;">犯罪・刑事事件</div>
    <div class="practice-tag" style="left:916px; top:142px; width:236px;">行政事件</div>

    <div class="feature feature--same-day" style="left:30px;">即日<br>相談可</div>
    <div class="feature feature--night" style="left:258px;">夜間<br>相談可</div>
    <div class="feature feature--station" style="left:502px;"><span>北浦駅<small>(みなと橋)</small>近く</span></div>
    <div class="feature feature--record" style="left:736px;">豊富な<br>相談実績</div>
    <div class="feature feature--payment" style="left:968px;">分割・後払<br>可</div>

    <p class="consult-band">そのお悩みお気軽にご相談ください。</p>

    <div class="firm-bar">
      <span class="firm-name">榊原誠一法律事務所</span>
    </div>
  </div>
</body>
</html>
```